BrivoMatex. Lantern for the Steady Growth. Business card

Professional business card for BrivoMatex (Lantern for the Steady Growth)
My rationale: Strategy-> Execution-> Results-> Value that lead to the BrivoMatex name: We put the Lantern for the Steady Growth.
We deliver value to our customers helping them at defining a good strategy (cyan arrow). 90% of well formulated strategies fail due to poor execution so we also consider strategical execution very important (green arrow). Due to the execution we obtain the results (blue arrow). Finally, the results provide feedback to redefine strategy, and the new strategy has to be executed and new results obtained providing new feedback and on and on. It's like a wheel that finally, must create corporate value: value for shareholders, staholders, employees, providers...-

Target Market(s)

CEOs and steering comitees , invewrnent funds

Industry/Entity Type

Business Consultant

Contact Information for Business Card

Tommaso Ferlini
CEO & Founder
tommaso.ferlini@brivomatex.example
Mobile: +34 611.205.938
www.brivomatex.example

Colors

Designer to choose colors to be used in the design.

Requirements
Nice to have
• Nice to hace the words: Strategy, execution, results
• Nice to vave the claim: Lantern for the Steady Growth
• The three colors should be shown:
• cyan for STRATEGY
• green for EXECUTION
• blue for RESULTS
Should not have
• Complete black background

```html
<!DOCTYPE html>
<html lang="en">
<head>
<meta charset="UTF-8">
<title>BrivoMatex – Business Card</title>
<link rel="stylesheet" href="https://fonts.googleapis.com/css2?family=Arimo:wght@400;700&family=Open+Sans:wght@400;600&display=swap">
<style>
  :root {
    --navy: #0a3290;
    --cyan: #12b1ea;
    --green: #8cc63f;
    --white: #ffffff;
    --grey-text: #3a3a3a;
    --backdrop: #e6e8ec;
    --card-shadow: 0 10px 30px rgba(0, 0, 0, 0.18);
  }
  * { margin: 0; padding: 0; box-sizing: border-box; }
  html, body {
    width: 1200px;
    height: 960px;
    overflow: hidden;
    background: var(--backdrop);
  }
  .canvas {
    width: 1200px;
    height: 960px;
    display: flex;
    flex-direction: column;
    align-items: center;
    justify-content: center;
    gap: 50px;
  }
  .card {
    position: relative;
    width: 700px;
    height: 400px;
    background: var(--white);
    box-shadow: var(--card-shadow);
    overflow: hidden;
  }
  .wordmark {
    font-family: "Arimo", Arial, sans-serif;
    font-weight: 700;
    color: var(--navy);
    letter-spacing: -1px;
    line-height: 1;
  }

  /* Back side */
  .card-back {
    display: flex;
    flex-direction: column;
    align-items: center;
    justify-content: center;
  }
  .card-back .wordmark { font-size: 82px; }
  .card-back .site {
    margin-top: 34px;
    font-family: "Open Sans", Arial, sans-serif;
    font-size: 19px;
    letter-spacing: 3px;
    color: var(--grey-text);
  }
  .card-back .site strong { color: var(--navy); font-weight: 600; }

  /* Front side */
  .card-front .waves {
    position: absolute;
    inset: 0;
    width: 700px;
    height: 400px;
  }
  .card-front .wordmark {
    position: absolute;
    left: 44px;
    top: 62px;
    font-size: 58px;
  }
  .person {
    position: absolute;
    right: 40px;
    top: 118px;
    text-align: right;
    font-family: "Arimo", Arial, sans-serif;
  }
  .person-name {
    font-size: 24px;
    font-weight: 700;
    color: var(--navy);
  }
  .person-role {
    margin-top: 6px;
    font-size: 15px;
    color: var(--grey-text);
  }
  .contact {
    position: absolute;
    right: 36px;
    bottom: 20px;
    list-style: none;
    font-family: "Open Sans", Arial, sans-serif;
    font-size: 16px;
    color: var(--white);
    text-align: right;
    z-index: 1;
  }
  .contact li {
    display: flex;
    align-items: center;
    justify-content: flex-end;
    gap: 10px;
    height: 27px;
  }
  .contact svg { width: 16px; height: 16px; flex: none; }
</style>
</head>
<body>
<main class="canvas">

  <section class="card card-back" aria-label="Business card, back">
    <div class="wordmark">BrivoMatex</div>
    <p class="site">www.<strong>brivomatex</strong>.example</p>
  </section>

  <section class="card card-front" aria-label="Business card, front">
    <svg class="waves" viewBox="0 0 700 400" aria-hidden="true">
      <path d="M0,172 C70,185 150,235 230,280 C160,256 80,224 0,214 Z" fill="var(--green)"/>
      <path d="M0,226 C150,276 260,306 360,298 C480,288 600,240 700,212 L700,220 C600,250 480,298 360,308 C260,316 150,290 0,240 Z" fill="var(--cyan)"/>
      <path d="M0,250 C150,300 260,330 360,322 C480,312 600,262 700,232 L700,400 L0,400 Z" fill="var(--navy)"/>
    </svg>

    <div class="wordmark">BrivoMatex</div>

    <div class="person">
      <p class="person-name">Tommaso Ferlini</p>
      <p class="person-role">CEO &amp; Founder</p>
    </div>

    <ul class="contact">
      <li>+34 611.205.938
        <svg viewBox="0 0 16 16" aria-label="Mobile"><rect x="4" y="1" width="8" height="14" rx="1.5" fill="none" stroke="var(--green)" stroke-width="1.6"/><circle cx="8" cy="12.3" r="0.9" fill="var(--green)"/></svg>
      </li>
      <li>www.brivomatex.example
        <svg viewBox="0 0 16 16" aria-label="Website"><circle cx="8" cy="8" r="6.5" fill="none" stroke="var(--green)" stroke-width="1.5"/><ellipse cx="8" cy="8" rx="3" ry="6.5" fill="none" stroke="var(--green)" stroke-width="1.2"/><path d="M1.5,8 H14.5" stroke="var(--green)" stroke-width="1.2"/></svg>
      </li>
      <li>tommaso.ferlini@brivomatex.example
        <svg viewBox="0 0 16 16" aria-label="Email"><rect x="1" y="3" width="14" height="10" fill="var(--green)"/><path d="M1,3 L8,9 L15,3" fill="none" stroke="var(--navy)" stroke-width="1.3"/></svg>
      </li>
    </ul>
  </section>

</main>
</body>
</html>
```